Wageline Associates Business Card Design

We need a business card designed around our new logo. The business card should be modern in design & should communicate success, confidence, power, sophistication. The target market is young business professionals. This is for a human resource & payroll outsourcing business.

```html
<!DOCTYPE html>
<html lang="en">
<head>
<meta charset="utf-8">
<title>Wageline Associates Business Card</title>
<link rel="stylesheet" href="https://fonts.googleapis.com/css2?family=Roboto:wght@400;500;700&display=swap">
<style>
  :root {
    --bg-light: #8f9aa0;
    --bg-dark: #4a5459;
    --card-white: #ffffff;
    --ink: #111111;
    --accent-red: #e3191f;
    --band-black: #000000;
    --text-light: #ffffff;
  }
  * { box-sizing: border-box; margin: 0; padding: 0; }
  html, body { width: 1200px; height: 900px; overflow: hidden; }
  body {
    background: radial-gradient(ellipse at 50% 45%, var(--bg-light), var(--bg-dark));
    font-family: "Roboto", Arial, sans-serif;
    position: relative;
  }
  .card {
    position: absolute;
    left: 250px;
    width: 700px;
    height: 400px;
    background: var(--card-white);
    box-shadow: 0 8px 22px rgba(0,0,0,0.35);
    overflow: hidden;
  }
  .card--front { top: 30px; }
  .card--back { top: 470px; }

  .brand {
    display: flex;
    align-items: center;
    gap: 10px;
    color: var(--ink);
    font-weight: 500;
    letter-spacing: 0.5px;
    white-space: nowrap;
  }
  .brand__dot {
    width: 20px; height: 20px; border-radius: 50%;
    background: var(--accent-red);
    flex: none;
  }
  .card--front .brand {
    position: absolute; left: 0; right: 0; top: 165px;
    justify-content: center;
    font-size: 42px;
  }
  .front__web {
    position: absolute; left: 380px; top: 322px;
    font-size: 15px; color: var(--ink);
  }

  .back__wave { position: absolute; inset: 0; width: 700px; height: 400px; }
  .card--back .brand {
    position: absolute; left: 50px; top: 92px;
    font-size: 29px;
  }
  .card--back .brand__dot { width: 16px; height: 16px; }
  .person {
    position: absolute; right: 70px; top: 30px; text-align: right;
  }
  .person__name { font-size: 19px; font-weight: 700; color: var(--ink); letter-spacing: 0.3px; }
  .person__role { font-size: 11px; font-weight: 700; color: var(--accent-red); }

  .contact {
    position: absolute; right: 40px; top: 160px;
    list-style: none;
    color: var(--text-light);
    font-size: 15px;
    text-align: right;
  }
  .contact__item {
    display: flex; align-items: center; justify-content: flex-end;
    gap: 10px; height: 25px;
  }
  .contact__icon {
    width: 18px; height: 18px; background: var(--text-light);
    display: flex; align-items: center; justify-content: center;
  }
  .contact__icon svg { width: 13px; height: 13px; }

  .address {
    position: absolute; left: 175px; bottom: 22px;
    color: var(--text-light); font-size: 16px; line-height: 1.35;
  }
</style>
</head>
<body>

<section class="card card--front" aria-label="Card front">
  <div class="brand"><span class="brand__dot"></span><span class="brand__name">Wageline Associates</span></div>
  <p class="front__web">www.wagelineassoc.com</p>
</section>

<section class="card card--back" aria-label="Card back">
  <svg class="back__wave" viewBox="0 0 700 400" aria-hidden="true">
    <path d="M0,285 C170,300 260,270 340,200 C420,125 520,95 700,80 L700,400 L0,400 Z" fill="var(--band-black)"/>
    <path d="M0,285 C170,300 260,270 340,200 C420,125 520,95 700,80" fill="none" stroke="var(--accent-red)" stroke-width="4"/>
    <path d="M0,330 C130,330 230,300 300,250 C230,290 130,315 0,318 Z" fill="var(--text-light)"/>
    <path d="M0,338 C140,340 250,305 320,245 C250,300 140,330 0,334 Z" fill="var(--accent-red)"/>
    <path d="M360,205 C440,140 540,112 660,100" fill="none" stroke="var(--accent-red)" stroke-width="2"/>
  </svg>

  <div class="brand"><span class="brand__dot"></span><span class="brand__name">Wageline Associates</span></div>

  <div class="person">
    <p class="person__name">DANIEL REYES</p>
    <p class="person__role">OWNER</p>
  </div>

  <ul class="contact">
    <li class="contact__item">555-204-7781
      <span class="contact__icon"><svg viewBox="0 0 24 24"><path d="M6.6 10.8a15 15 0 0 0 6.6 6.6l2.2-2.2a1 1 0 0 1 1-.25 11.4 11.4 0 0 0 3.6.6 1 1 0 0 1 1 1V20a1 1 0 0 1-1 1A17 17 0 0 1 3 4a1 1 0 0 1 1-1h3.5a1 1 0 0 1 1 1c0 1.250.2 2.450.6 3.6a1 1 0 0 1-.25 1z" fill="#000"/></svg></span></li>
    <li class="contact__item">555-204-7782
      <span class="contact__icon"><svg viewBox="0 0 24 24"><rect x="4" y="9" width="16" height="11" rx="1" fill="#000"/><path d="M3 8c3-4 15-4 18 0v2h-4V8H7v2H3z" fill="#000"/></svg></span></li>
    <li class="contact__item">hello@wagelineassoc.com
      <span class="contact__icon"><svg viewBox="0 0 24 24"><rect x="3" y="5" width="18" height="14" fill="#000"/><path d="M3 5l9 8 9-8" fill="none" stroke="#fff" stroke-width="1.6"/></svg></span></li>
    <li class="contact__item">www.wagelineassoc.com
      <span class="contact__icon"><svg viewBox="0 0 24 24"><circle cx="12" cy="12" r="9" fill="none" stroke="#000" stroke-width="2"/><path d="M3 12h18M12 3c-4 4-4 14 0 18M12 3c4 4 4 14 0 18" fill="none" stroke="#000" stroke-width="1.6"/></svg></span></li>
  </ul>

  <p class="address">Level 3 Harbour View Plaza<br>Quay Street, Suva, Fiji</p>
</section>

</body>
</html>
```